Business Card Design for general contractor or developer

General Contractors. We build new buildings as well as redesign and/or remodel existing buildings. Mostly residential, but we want to expand to commercial as well, so we want the design not to be residential specific.We want the design to be modern, but necessarily minimalistic. A monogram type is also a consideration, but would like to see all ideas.

Target Market(s)

Real estate investors, homeowners, future homeowners, commercial building owners

Industry/Entity Type

Contractor

Contact Information for Business Card

BRIMCOVE Developers Corp, 6127 NE 318th Avenue Suite 241 Miami Lakes, FL 33482, Curtis Ortega, (305) 472-1803, curtis@quarvinta.com

Font styles to use
Other font styles liked:
• Modern type font

Requirements
Must have
• Must be modern looking
Nice to have
• Metallic type or a standout feature
Should not have
• Tools, floorplans

```html
<!DOCTYPE html>
<html lang="en">
<head>
<meta charset="utf-8">
<title>BRIMCOVE Developers Corp – Business Card</title>
<link href="https://fonts.googleapis.com/css2?family=Exo+2:wght@400;700&display=swap" rel="stylesheet">
<style>
  :root {
    --backdrop: #e9e6e1;
    --card-white: #ffffff;
    --ink-blue: #2a63c4;
    --deep-blue: #1746a0;
    --bright-blue: #2f86d6;
    --text-grey: #6d6d6d;
    --mark-white: #ffffff;
  }
  * { margin: 0; padding: 0; box-sizing: border-box; }
  html, body {
    width: 1200px; height: 885px; overflow: hidden;
    background: var(--backdrop);
    font-family: "Exo 2", sans-serif;
  }
  .stage {
    position: relative; width: 1200px; height: 885px;
    display: flex; justify-content: center; align-items: center; gap: 90px;
  }
  .card {
    width: 380px; height: 660px; border-radius: 6px;
    position: relative; overflow: hidden;
    box-shadow: 0 12px 30px rgba(0,0,0,.18);
  }
  .card-front { background: var(--card-white); }
  .card-front .base-band {
    position: absolute; left: 0; right: 0; bottom: 0; height: 96px;
    background: linear-gradient(90deg, var(--deep-blue), var(--bright-blue) 55%, var(--deep-blue));
  }
  .brand {
    display: flex; flex-direction: column; align-items: center;
  }
  .brand-dot {
    width: 96px; height: 96px; border-radius: 50%;
    background: var(--ink-blue);
  }
  .brand-name {
    margin-top: 18px; text-align: center;
    font-weight: 700; color: var(--ink-blue);
    font-size: 34px; letter-spacing: 2px; line-height: 1.1;
  }
  .brand-name .sub { display: block; font-size: 22px; letter-spacing: 1px; }
  .card-front .brand { margin-top: 70px; }
  .contact { text-align: center; margin-top: 44px; }
  .contact .person {
    color: var(--ink-blue); font-weight: 700; font-size: 28px; margin-bottom: 20px;
  }
  .contact p {
    color: var(--text-grey); font-size: 16px; line-height: 1.55;
  }
  .contact .address { margin-top: 14px; }
  .card-back {
    background: radial-gradient(circle at 50% 40%, var(--bright-blue), var(--deep-blue) 75%);
    display: flex; align-items: center; justify-content: center;
  }
  .card-back .brand-dot { background: var(--mark-white); width: 120px; height: 120px; }
  .card-back .brand-name { color: var(--mark-white); font-size: 38px; }
  .card-back .brand-name .sub { font-size: 25px; }
</style>
</head>
<body>
<main class="stage">
  <section class="card card-front">
    <div class="brand">
      <div class="brand-dot"></div>
      <div class="brand-name">BRIMCOVE<span class="sub">Developers Corp</span></div>
    </div>
    <div class="contact">
      <h1 class="person">Curtis Ortega</h1>
      <p>(305) 472-1803</p>
      <p>curtis@quarvinta.com</p>
      <p class="address">6127 NE 318th Avenue Suite 241<br>Miami Lakes, FL 33482</p>
    </div>
    <div class="base-band"></div>
  </section>
  <section class="card card-back">
    <div class="brand">
      <div class="brand-dot"></div>
      <div class="brand-name">BRIMCOVE<span class="sub">Developers Corp</span></div>
    </div>
  </section>
</main>
</body>
</html>
```